Maple Hollow Skilled Nursing Facility

We are a skilled nursing facility that cares for elderly when they have come from the hospital and are trying to transition to make it back to their homes! We strive to create an environment that is friendly with great service to meet their needs and take care of them. The task is to create a website that informs the community of our excellent service and care. I will upload our logo and a brochure to give some ideas.
Target Market(s)
Families who will be looking at care facilities and rating them based on their quality for their loved ones.
Coding
Coded - Design and coding required
Number of Pages Required
5+ page
Requirements
Must have
- Social Media Integration.
Nice to have
- Nice, professional and clean. A warming website that is inviting to those who see.

```html
<!DOCTYPE html>
<html lang="en">
<head>
<meta charset="utf-8">
<title>Maple Hollow Post Acute</title>
<link href="https://fonts.googleapis.com/css2?family=Cinzel:wght@400;700&family=Lato:ital,wght@0,400;0,700;1,400&display=swap" rel="stylesheet">
<style>
:root{
  --blue:#0a5fc9;
  --green:#7cc11c;
  --orange:#f26a12;
  --ink:#1d1d1d;
  --text:#2b2b2b;
  --footer:#2c363d;
  --footer-line:#465159;
  --white:#fff;
}
*{box-sizing:border-box;margin:0;padding:0}
html,body{width:1200px;height:2446px;overflow:hidden}
body{position:relative;background:var(--white);font-family:"Lato",sans-serif;color:var(--text)}

/* header */
.site-header{position:absolute;left:0;top:0;width:1200px;height:110px;background:var(--white);border-top:3px solid var(--orange)}
.brand{position:absolute;left:80px;top:28px;display:flex;align-items:center;gap:14px}
.brand-mark{width:52px;height:52px;border-radius:50%;background:var(--blue)}
.brand-name{font-family:"Cinzel",serif;font-size:30px;line-height:1;color:var(--ink);font-weight:400}
.brand-sub{font-size:18px;letter-spacing:2px}
.phone-tab{position:absolute;left:898px;top:0;width:206px;height:36px;background:var(--orange);border-radius:0 0 26px 26px;color:var(--white);font-size:18px;font-weight:700;display:flex;align-items:center;justify-content:center;gap:10px}
.main-nav{position:absolute;left:536px;top:52px;display:flex;gap:23px;font-size:18px;color:#333}
.main-nav a{color:inherit;text-decoration:none;padding-bottom:4px}
.main-nav a.active{border-top:2px solid #555;border-bottom:2px solid #555;padding:2px 2px}

/* hero */
.hero{position:absolute;left:0;top:110px;width:1200px;height:602px;background:linear-gradient(100deg,#cfd8e3 0%,#e7e9ec 40%,#f2efea 60%,#d9dde2 100%)}
.hero-caption{position:absolute;left:0;top:478px;width:1200px;text-align:center;font-family:"Cinzel",serif;font-weight:700;font-size:34px;line-height:40px;color:var(--ink)}
.dots{position:absolute;display:flex;gap:12px}
.dots span{width:11px;height:11px;border-radius:50%;background:var(--blue)}
.dots span.on{background:var(--ink)}

/* welcome */
.welcome-title{position:absolute;left:0;top:752px;width:1200px;text-align:center;font-family:"Cinzel",serif;font-size:36px;color:var(--ink)}
.welcome-title em{font-style:normal;color:var(--blue)}
.divider{position:absolute;top:837px;height:1px;background:#bbb;width:280px}
.divider-dot{position:absolute;left:582px;top:820px;width:34px;height:34px;border-radius:50%;background:var(--blue)}
.welcome-text{position:absolute;left:96px;top:886px;width:1008px;text-align:center;font-size:16.5px;line-height:26px;color:var(--ink)}

/* services */
.service-band{position:absolute;left:0;top:1230px;width:1200px;height:217px;background:var(--blue)}
.service{position:absolute;top:1025px;width:330px}
.service-photo{width:330px;height:260px;border:3px solid var(--green);position:relative}
.service-badge{position:absolute;left:110px;bottom:-3px;width:104px;height:52px;border-radius:52px 52px 0 0;background:var(--green);display:flex;align-items:flex-end;justify-content:center;padding-bottom:10px}
.service-title{margin-top:28px;text-align:center;font-family:"Cinzel",serif;font-weight:400;font-size:29px;color:var(--white);letter-spacing:1px}
.read-more{display:flex;align-items:center;justify-content:space-between;margin:22px auto 0;width:136px;height:36px;border-radius:18px;background:var(--orange);border:2px solid var(--white);color:var(--white);font-size:14px;font-weight:700;padding:0 6px 0 18px}
.read-more i{width:24px;height:24px;border-radius:50%;background:var(--white);display:flex;align-items:center;justify-content:center}

/* specialities + testimonials */
.split{position:absolute;top:1447px;height:433px}
.specialities{left:0;width:595px;background:linear-gradient(90deg,#f4f4f4,#e6e6e6)}
.doctor-photo{position:absolute;left:0;top:0;width:300px;height:433px;background:linear-gradient(180deg,#efe8de 0%,#f5f4f2 45%,#e2e6ea 100%)}
.section-title{position:absolute;font-size:31px;font-weight:700;color:var(--blue)}
.section-title em{font-style:normal;color:var(--green);font-weight:400}
.spec-list{position:absolute;right:38px;top:100px;list-style:none;text-align:right;font-size:15.5px;line-height:25.7px;color:var(--ink)}
.spec-list li{display:flex;justify-content:flex-end;align-items:center;gap:14px}
.testimonials{left:595px;width:605px;background:linear-gradient(90deg,#ededed,#f6f6f6)}
.elder-photo{position:absolute;right:0;top:0;width:300px;height:433px;background:linear-gradient(180deg,#eeeeee 0%,#e9e4dc 50%,#d9d2c6 100%)}
.quote{position:absolute;left:32px;top:106px;width:292px;font-style:italic;font-size:15.5px;line-height:28.5px;color:var(--ink)}
.quote-mark{font-family:Georgia,serif;font-size:42px;color:#777;font-style:normal;line-height:0;vertical-align:-14px}
.quote-rule{position:absolute;left:32px;top:320px;width:200px;height:1px;background:#bbb}
.client-name{position:absolute;left:36px;top:332px;font-size:19px;font-weight:700;color:var(--blue)}
.client-role{position:absolute;left:36px;top:358px;font-size:13px;color:var(--ink)}

/* tagline */
.tagline{position:absolute;left:60px;top:1926px;width:1080px;text-align:center;font-family:"Cinzel",serif;font-size:23px;line-height:34px;color:var(--blue)}

/* footer */
.footer-shape{position:absolute;left:0;top:2030px;width:1200px;height:372px}
.footer-badge{position:absolute;left:567px;top:2025px;width:66px;height:66px;border-radius:50%;background:var(--white);border:4px solid var(--white);box-shadow:0 0 0 1px #ccc}
.footer-badge span{display:block;width:100%;height:100%;border-radius:50%;background:var(--blue)}
.footer-col{position:absolute;top:2132px;color:#e8e8e8;font-size:13.5px}
.footer-col h3{font-weight:400;font-size:22px;color:var(--white);padding-bottom:10px;border-bottom:1px solid var(--footer-line);margin-bottom:16px}
.footer-col h3 em{font-style:normal;color:var(--green)}
.footer-links{list-style:none;line-height:29.3px}
.footer-links li::before{content:"";display:inline-block;width:4px;height:4px;border-radius:50%;background:var(--green);margin-right:10px;vertical-align:middle}
.contact-line{display:flex;align-items:center;gap:10px;margin-top:14px}
.field{width:268px;height:34px;background:var(--white);border-radius:2px;margin-bottom:8px;color:#333;font-size:13px;padding:9px 12px}
.submit{width:124px;height:36px;border-radius:3px;background:linear-gradient(#8fd12a,#6aa815);color:var(--white);font-weight:700;font-size:17px;text-align:center;line-height:36px;margin-top:4px}
.social{list-style:none}
.social li{display:flex;align-items:center;gap:12px;height:43px;font-size:13px;font-weight:700;white-space:nowrap}
.social i{width:32px;height:32px;border-radius:50%;flex:none}
.col-rule{position:absolute;top:2132px;width:1px;height:230px;background:var(--footer-line)}
.copyright{position:absolute;left:0;top:2402px;width:1200px;height:44px;background:var(--blue);color:var(--white);font-size:13px;font-weight:700;text-align:center;line-height:44px}
</style>
</head>
<body>

<header class="site-header">
  <div class="brand"><span class="brand-mark"></span><span class="brand-name">Maple Hollow<br><span class="brand-sub">Post Acute</span></span></div>
  <div class="phone-tab">
    <svg width="20" height="20" viewBox="0 0 20 20"><circle cx="10" cy="10" r="10" fill="#fff"/><path d="M6.5 5.2l1.8-.4 1 2.4-1.2 1a7 7 0 0 0 3.6 3.6l1-1.2 2.4 1-.4 1.8c-4.6.3-8.5-3.6-8.2-8.2z" fill="#f26a12"/></svg>
    (555) 214-7380
  </div>
  <nav class="main-nav">
    <a class="active" href="#">Home</a><a href="#">About Us</a><a href="#">Services</a><a href="#">Resources</a><a href="#">Testimonials</a><a href="#">Contact Us</a>
  </nav>
</header>

<section class="hero" role="img" aria-label="Photo of a smiling nurse with a stethoscope caring for an elderly woman">
  <p class="hero-caption">We Provide the top quality nursing care and<br>Rehabilitaion services to the Harbor County Community</p>
  <div class="dots" style="left:572px;top:569px"><span></span><span class="on"></span><span></span></div>
</section>

<h1 class="welcome-title">Welcome to <em>Maple Hollow</em> Post Acute</h1>
<div class="divider" style="left:290px"></div>
<div class="divider" style="left:630px"></div>
<div class="divider-dot"></div>
<p class="welcome-text">Maple Hollow Post Acute is a HCQ 5 Star Rated, 149 bed, Skilled Nursing Facility located in tranquil Fernwood. We seek to provide top quality nursing care and rehabilitation services to the Harbor County community. We specialize in post-hospital rehab and recovery that will get patients from hospital to home in a comfortable and productive environment. We are licensed and contracted to accept SeniorShield, Valemed and most Managed Care plans.</p>

<div class="service-band"></div>

<article class="service" style="left:80px">
  <div class="service-photo" role="img" aria-label="Photo of a caregiver holding an elderly patient's hands" style="background:linear-gradient(135deg,#5fb0dc,#e9d8c6 55%,#a9c96a)">
    <span class="service-badge"><svg width="30" height="30" viewBox="0 0 30 30"><circle cx="15" cy="15" r="13" fill="none" stroke="#fff" stroke-width="2.5"/><path d="M15 9v12M9 15h12" stroke="#fff" stroke-width="3"/></svg></span>
  </div>
  <h2 class="service-title">Nursing Care</h2>
  <a class="read-more">Read More <i><svg width="10" height="10" viewBox="0 0 10 10"><path d="M3 1l4 4-4 4" stroke="#f26a12" stroke-width="2" fill="none"/></svg></i></a>
</article>

<article class="service" style="left:436px">
  <div class="service-photo" role="img" aria-label="Photo of a therapist treating a patient's knee" style="background:linear-gradient(135deg,#f4f4f4,#efc9a8 50%,#8fa7c6)">
    <span class="service-badge"><svg width="30" height="30" viewBox="0 0 30 30"><circle cx="15" cy="15" r="13" fill="none" stroke="#fff" stroke-width="2.5"/><path d="M15 9v12M9 15h12" stroke="#fff" stroke-width="3"/></svg></span>
  </div>
  <h2 class="service-title">Rehabilitation</h2>
  <a class="read-more">Read More <i><svg width="10" height="10" viewBox="0 0 10 10"><path d="M3 1l4 4-4 4" stroke="#f26a12" stroke-width="2" fill="none"/></svg></i></a>
</article>

<article class="service" style="left:791px">
  <div class="service-photo" role="img" aria-label="Photo of a physical therapist stretching a patient's arm" style="background:linear-gradient(135deg,#d8c3a8,#f08a6a 45%,#6c8d5a)">
    <span class="service-badge"><svg width="30" height="30" viewBox="0 0 30 30"><circle cx="15" cy="15" r="13" fill="none" stroke="#fff" stroke-width="2.5"/><path d="M15 9v12M9 15h12" stroke="#fff" stroke-width="3"/></svg></span>
  </div>
  <h2 class="service-title">Therapy Services</h2>
  <a class="read-more">Read More <i><svg width="10" height="10" viewBox="0 0 10 10"><path d="M3 1l4 4-4 4" stroke="#f26a12" stroke-width="2" fill="none"/></svg></i></a>
</article>

<section class="split specialities">
  <div class="doctor-photo" role="img" aria-label="Photo of a smiling female doctor with a stethoscope"></div>
  <h2 class="section-title" style="left:318px;top:30px">We <em>Specialize In</em></h2>
  <ul class="spec-list">
    <li>Physical, Occupational &amp; Speech Therapy<svg width="18" height="16"><path d="M2 8l5 5 9-11" stroke="#7cc11c" stroke-width="3" fill="none"/></svg></li>
    <li>Post Surgery Rehabilitation<svg width="18" height="16"><path d="M2 8l5 5 9-11" stroke="#7cc11c" stroke-width="3" fill="none"/></svg></li>
    <li>Total Hip and Knee Replacement<svg width="18" height="16"><path d="M2 8l5 5 9-11" stroke="#7cc11c" stroke-width="3" fill="none"/></svg></li>
    <li>Back Surgery Recovery<svg width="18" height="16"><path d="M2 8l5 5 9-11" stroke="#7cc11c" stroke-width="3" fill="none"/></svg></li>
    <li>Orthopedic Rehabilitation<svg width="18" height="16"><path d="M2 8l5 5 9-11" stroke="#7cc11c" stroke-width="3" fill="none"/></svg></li>
    <li>Status Post Fractures<svg width="18" height="16"><path d="M2 8l5 5 9-11" stroke="#7cc11c" stroke-width="3" fill="none"/></svg></li>
    <li>Stroke Recovery<svg width="18" height="16"><path d="M2 8l5 5 9-11" stroke="#7cc11c" stroke-width="3" fill="none"/></svg></li>
    <li>Cardiac Wellness Rehabilitation<svg width="18" height="16"><path d="M2 8l5 5 9-11" stroke="#7cc11c" stroke-width="3" fill="none"/></svg></li>
    <li>New Assistive Device Training<svg width="18" height="16"><path d="M2 8l5 5 9-11" stroke="#7cc11c" stroke-width="3" fill="none"/></svg></li>
    <li>Prosthetics Training<svg width="18" height="16"><path d="M2 8l5 5 9-11" stroke="#7cc11c" stroke-width="3" fill="none"/></svg></li>
    <li>Fall Prevention<svg width="18" height="16"><path d="M2 8l5 5 9-11" stroke="#7cc11c" stroke-width="3" fill="none"/></svg></li>
    <li>Vestibular Rehabilitation<svg width="18" height="16"><path d="M2 8l5 5 9-11" stroke="#7cc11c" stroke-width="3" fill="none"/></svg></li>
  </ul>
</section>

<section class="split testimonials">
  <div class="elder-photo" role="img" aria-label="Photo of a smiling elderly woman resting her chin on her hand"></div>
  <h2 class="section-title" style="left:30px;top:30px">Client <em>Testimonials</em></h2>
  <p class="quote"><span class="quote-mark">&ldquo;</span> Lorem ipsum dolor sit amet, consectetuer adipiscing elit, sed diam nonummy nibh euismod tincidunt ut laoreet dolore magna aliquam erat volutpat. Ut wisi enim ad minim veniam, quis nostrud exerci tation ullamcorper suscipit lobortis nisl ut aliquip adipiscing elit, seerwer <span class="quote-mark">&rdquo;</span></p>
  <div class="quote-rule"></div>
  <p class="client-name">Helen Marsh</p>
  <p class="client-role">Lorem ipsum</p>
  <div class="dots" style="left:38px;top:394px;gap:5px"><span style="width:7px;height:7px" class="on"></span><span style="width:7px;height:7px" class="on"></span><span style="width:7px;height:7px"></span></div>
</section>

<p class="tagline">We are a skilled nursing facility that trive to create an environment that is<br>friendly with great service to meet their needs and take care of them.</p>

<svg class="footer-shape" viewBox="0 0 1200 372" preserveAspectRatio="none">
  <path d="M0 90 Q600 -20 1200 90 V372 H0Z" fill="#2c363d"/>
</svg>
<div class="footer-badge"><span></span></div>

<div class="footer-col" style="left:82px;width:178px">
  <h3>Quick <em>Links</em></h3>
  <ul class="footer-links"><li>Home</li><li>About Us</li><li>Services</li><li>Resources</li><li>Testimonials</li><li>Contact Us</li></ul>
</div>
<div class="col-rule" style="left:260px"></div>
<div class="footer-col" style="left:313px;width:230px">
  <h3>Contact <em>Details</em></h3>
  <p style="font-size:15px">Maple Hollow Post Acute</p>
  <p style="line-height:19px;margin-top:6px">123, Ut wisi enim ad minim veniam,<br>Mor nostrni tation -123 456</p>
  <p class="contact-line"><svg width="13" height="13" viewBox="0 0 20 20"><path d="M4 2l4 0 1 5-2 2a11 11 0 0 0 4 4l2-2 5 1v4c-9 1-15-5-14-14z" fill="#7cc11c"/></svg>(555) 214-7380</p>
  <p class="contact-line"><svg width="14" height="12" viewBox="0 0 14 12"><rect x="3" y="0" width="8" height="4" fill="#7cc11c"/><rect x="0" y="4" width="14" height="5" fill="#7cc11c"/><rect x="3" y="8" width="8" height="4" fill="#7cc11c"/></svg>(555) 214-7391 ; 7392</p>
  <p class="contact-line" style="font-size:12.5px"><svg width="13" height="10" viewBox="0 0 13 10"><rect width="13" height="10" fill="#7cc11c"/><path d="M0 0l6.5 5L13 0" stroke="#2c363d" fill="none"/></svg>Inquiry@maplehollowpostacute.com</p>
</div>
<div class="col-rule" style="left:592px"></div>
<div class="footer-col" style="left:640px;width:268px">
  <h3>Quick <em>Inquiry</em></h3>
  <div class="field">Name</div><div class="field">Email</div><div class="field">Message</div>
  <div class="submit">Submit</div>
</div>
<div class="col-rule" style="left:952px"></div>
<div class="footer-col" style="left:1003px;width:140px">
  <h3>Follow <em>Us</em></h3>
  <ul class="social">
    <li><i style="background:#1f5cb5"></i>FRIENDLINE</li>
    <li><i style="background:#22b3e8"></i>CHIRPER</li>
    <li><i style="background:#1b73b3"></i>WORKLINK</li>
    <li><i style="background:#f39a1d"></i>GLOBECAST</li>
  </ul>
</div>

<footer class="copyright">Copyright © 2016 Maple Hollow Post Acute. All Rights Reserved.</footer>

</body>
</html>
```